Website Design for Freeze-Dried Food Manufacturing Company (Pet Food & Agri-Food)

We are looking for a high-level web designer to create a clean, modern, premium website design for Brindle, a freeze-dried food manufacturing company operating in both the pet food and agri-food space.
This is not a basic website build β we are looking for a designer who understands brand positioning, layout, and user flow, not just visuals.
π― Project Objective
Design a website that:
Clearly communicates our capabilities and value proposition
Feels premium, credible, and product-driven
Guides users through a simple, intuitive journey
Clean and Crips
A critical requirement is clearly separating:
π Pet Food
π Agri-Food
These must feel like two distinct pathways within the same brand experience.
We have attached detailed documents outlining structure, layout, and messaging. These should be followed closely.
π What Success Looks Like
A high-impact homepage with strong visual hierarchy
Clear entry points into Pet Food and Agri-Food
Clean, intentional layout (not cluttered or template-like)
Thoughtful spacing, typography, and flow
A design that feels considered and elevated, not generic
π¨ Design Direction
We are aiming for a:
Minimal, premium aesthetic
Warm, natural color palette (creams, browns, muted tones)
Ingredient and product-focused visuals
Avoid:
Overly corporate / industrial styles
Generic SaaS-style layouts
Busy or over-designed interfaces
End Goal
A website that immediately communicates:
Who we are
What we do
Why weβre different
In a way that feels premium, clear, and easy to navigate.
Link to current website: https://brindleharvest.example/
https://brindlelabs.example/wp-admin/

```html
<!DOCTYPE html>
<html lang="en">
<head>
<meta charset="utf-8">
<title>Brindle — Nutrition, Frozen in Time</title>
<link href="https://fonts.googleapis.com/css2?family=Young+Serif&family=Inter:wght@400;500;600&display=swap" rel="stylesheet">
<style>
:root{
  --gold:#c9a567;
  --gold-dark:#b8934f;
  --cream:#faf8f4;
  --peach:#f8e9dc;
  --card-body:#e9dfd2;
  --ink:#2b2118;
  --muted:#6b6158;
  --soft:#9a9088;
  --band:#2f2419;
  --foot:#2a2017;
  --line:#ddd5cb;
}
*{margin:0;padding:0;box-sizing:border-box}
html,body{width:1200px;height:3912px;overflow:hidden}
body{background:var(--cream);font-family:"Inter",sans-serif;color:var(--ink);position:relative}
.serif{font-family:"Young Serif",serif}
.abs{position:absolute}
.btn{position:absolute;display:flex;align-items:center;justify-content:center;gap:14px;border-radius:6px;font-weight:600;font-size:14px;text-decoration:none}
.btn-gold{background:var(--gold);color:#fff}
.btn-line{border:1.5px solid #9c7a55;color:#7a5a3a;background:transparent}
.arrow{width:28px;height:10px}
.eyebrow{position:absolute;color:var(--gold);font-size:20px;letter-spacing:2px;font-weight:500}
.center{left:0;width:1200px;text-align:center}

/* nav */
.logo{left:50px;top:38px;font-size:29px;color:var(--gold)}
.nav{left:226px;top:46px;display:flex;gap:24px;font-size:14px;font-weight:500}
.nav a{color:var(--ink);text-decoration:none}
.nav a.active{border-bottom:2px solid var(--ink);padding-bottom:4px}

/* hero */
.hero-img{left:463px;top:109px;width:737px;height:568px;background:linear-gradient(180deg,#e8c99a 0%,#a9b07a 30%,#6f7a3c 60%,#4d5a28 100%)}
.hero-fade{left:463px;top:109px;width:200px;height:568px;background:linear-gradient(90deg,var(--cream),rgba(250,248,244,0))}
.hero-title{left:50px;top:246px;font-size:58px;line-height:68px}
.hero-sub{left:50px;top:412px;font-size:15px;font-weight:500}
.hero-body{left:50px;top:450px;font-size:14px;line-height:23px;color:var(--muted);width:430px}

/* category cards */
.cat{position:absolute;left:29px;width:1142px;background:var(--peach);border-radius:12px}
.cat-img{position:absolute;border-radius:4px}
.icon-circle{position:absolute;width:62px;height:62px;border-radius:50%;background:#fdf7f1;box-shadow:0 4px 10px rgba(120,90,60,.2);display:flex;align-items:center;justify-content:center}
.cat h2{position:absolute;font-weight:400;font-size:46px}
.cat p{position:absolute;font-size:13.5px;line-height:23px;color:var(--muted);width:500px}

/* dedicated */
.dedicated{left:29px;top:1580px;width:1142px;height:184px;border:1.5px solid var(--line)}
.dedicated h3{font-weight:400;font-size:22.5px;position:absolute;top:78px}
.dedicated p{position:absolute;top:116px;font-size:12px;line-height:23px;color:var(--soft)}

/* steps */
.step{position:absolute;top:2051px;width:150px;margin-left:-75px;text-align:center;font-size:15px;font-weight:500}
.step .ring{width:72px;height:72px;border:2px solid var(--gold);border-radius:50%;margin:0 auto 20px;display:flex;align-items:center;justify-content:center}
.chev{position:absolute;top:2092px;color:var(--gold);font-size:22px}

/* capabilities */
.cap{position:absolute;top:2394px;width:352px;height:419px;border-radius:12px;overflow:hidden;background:var(--card-body);box-shadow:0 14px 24px rgba(90,60,30,.15)}
.cap .img{height:206px}
.cap h4{font-size:21px;font-weight:500;margin:44px 34px 10px}
.cap p{font-size:12.5px;line-height:18px;color:var(--muted);margin:0 34px}
.cap .more{display:flex;align-items:center;gap:10px;margin:24px 34px 0;font-size:13px;font-weight:600;color:#5c4631}

/* why */
.why{position:absolute;top:3045px;width:230px;margin-left:-115px;text-align:center}
.why h5{font-size:21px;font-weight:500;line-height:27px;margin:18px 0 10px}
.why p{font-size:12.5px;line-height:18px;color:var(--muted)}

/* cta band */
.band{left:0;top:3342px;width:1200px;height:222px;background:var(--band)}
.band h2{position:absolute;left:46px;top:70px;color:var(--gold);font-weight:400;font-size:31px}
.band p{position:absolute;left:46px;top:122px;color:#eee3d4;font-size:14px;line-height:23px;width:500px}

/* footer */
.foot{left:0;top:3564px;width:1200px;height:348px;background:var(--foot);color:#e9dfd3}
.foot h6{position:absolute;top:100px;color:var(--gold);font-size:19px;font-weight:500;letter-spacing:.5px}
.foot ul{position:absolute;top:136px;list-style:none;font-size:14px;line-height:31px}
.social{position:absolute;top:242px;width:22px;height:22px;border:2px solid var(--gold);border-radius:3px}
</style>
</head>
<body>

<!-- header -->
<div class="abs logo serif">BRINDLE</div>
<nav class="abs nav">
  <a class="active" href="#">Home</a><a href="#">Our Story</a><a href="#">Applications</a><a href="#">Capabilities</a><a href="#">Quality &amp; Traceability</a><a href="#">Why Brindle</a><a href="#">Contact</a>
</nav>
<a class="btn btn-gold" style="left:984px;top:38px;width:166px;height:34px;font-size:13px">Start A Project <svg class="arrow" viewBox="0 0 28 10"><path d="M0 5h26M21 1l5 4-5 4" stroke="#fff" stroke-width="1.5" fill="none"/></svg></a>

<!-- hero -->
<div class="abs hero-img" role="img" aria-label="Aerial view of a white freeze-drying facility surrounded by green fields at golden hour"></div>
<div class="abs hero-fade"></div>
<div class="eyebrow" style="left:50px;top:217px">BRINDLE</div>
<h1 class="abs hero-title serif" style="font-weight:400">Nutrition,<br>Frozen in Time</h1>
<div class="abs hero-sub">Industrial Freeze-Drying &amp; Food Manufacturing</div>
<p class="abs hero-body">A fully integrated, closed-loop system from ingredient sourcing through to production, packaging, and distribution.</p>
<a class="btn btn-gold" style="left:50px;top:520px;width:170px;height:47px">Start A Project <svg class="arrow" viewBox="0 0 28 10"><path d="M0 5h26M21 1l5 4-5 4" stroke="#fff" stroke-width="1.5" fill="none"/></svg></a>

<!-- pet food -->
<section class="cat" style="top:778px;height:372px;background:linear-gradient(90deg,#f6ece2,#f9e8da)">
  <div class="cat-img" style="left:26px;top:22px;width:578px;height:327px;background:linear-gradient(180deg,#c9b49a,#b59a78 70%,#a88c6a)" role="img" aria-label="Golden retriever lying beside a metal bowl of freeze-dried pet food"></div>
  <div class="icon-circle" style="left:641px;top:62px"><svg width="18" height="16" viewBox="0 0 18 16" fill="#3a2a1c"><circle cx="4" cy="4" r="2"/><circle cx="9" cy="2.5" r="2"/><circle cx="14" cy="4" r="2"/><ellipse cx="9" cy="11" rx="5" ry="4"/></svg></div>
  <h2 class="serif" style="left:641px;top:134px">Pet Food</h2>
  <p style="left:641px;top:204px">Freeze-dried meals, toppers, and treats designed for quality, consistency, and performance.</p>
  <a class="btn btn-line" style="left:641px;top:267px;width:170px;height:47px">Start A Project <svg class="arrow" viewBox="0 0 28 10"><path d="M0 5h26M21 1l5 4-5 4" stroke="#7a5a3a" stroke-width="1.5" fill="none"/></svg></a>
</section>

<!-- agri food -->
<section class="cat" style="top:1177px;height:371px;background:linear-gradient(90deg,#f9e6d8,#f7efe7)">
  <div class="icon-circle" style="left:26px;top:56px"><svg width="16" height="16" viewBox="0 0 16 16" fill="#3a2a1c"><path d="M8 15V8M8 8C5 8 2 6 2 3c3 0 6 2 6 5zM8 8c3 0 6-2 6-5-3 0-6 2-6 5z" stroke="#3a2a1c" stroke-width="1.4"/></svg></div>
  <h2 class="serif" style="left:26px;top:129px">Agri-Food</h2>
  <p style="left:26px;top:200px">Freeze-dried meals, toppers, and treats designed for quality, consistency, and performance.</p>
  <a class="btn btn-line" style="left:26px;top:261px;width:170px;height:47px">Start A Project <svg class="arrow" viewBox="0 0 28 10"><path d="M0 5h26M21 1l5 4-5 4" stroke="#7a5a3a" stroke-width="1.5" fill="none"/></svg></a>
  <div class="cat-img" style="left:547px;top:23px;width:578px;height:325px;background:linear-gradient(180deg,#d9a659 0%,#8e7a4a 35%,#4c5a24 60%,#37461a 100%)" role="img" aria-label="Rows of green crops stretching toward hills at sunset"></div>
</section>

<!-- dedicated environment -->
<section class="abs dedicated">
  <div class="abs" style="left:32px;top:60px;width:84px;height:66px;border-radius:50% 8px;background:#ece4da" role="img" aria-label="Faint leaf decoration"></div>
  <div class="abs" style="left:1020px;top:56px;width:80px;height:74px;border-radius:45%;background:#ece4da" role="img" aria-label="Faint paw print decoration"></div>
  <svg class="abs" style="left:553px;top:14px" width="36" height="46" viewBox="0 0 36 46"><path d="M18 2 33 8v14c0 11-7 18-15 22C10 40 3 33 3 22V8z" fill="none" stroke="var(--gold)" stroke-width="3"/></svg>
  <h3 class="serif" style="left:0;width:1142px;text-align:center">Dedicated Production Environment</h3>
  <p style="left:0;width:1142px;text-align:center">Pet food and agri-food production are handled in separate, controlled environments to ensure<br>product integrity and category-specific&nbsp; standards</p>
</section>

<!-- closed loop -->
<div class="eyebrow center" style="top:1832px">CLOSED LOOP</div>
<h2 class="abs center serif" style="top:1868px;font-weight:400;font-size:38px">A Complete, Closed-Loop System</h2>
<p class="abs center" style="top:1936px;font-size:14px;line-height:23px;color:#4a4038">We manage every stage in-house, allowing full control over quality, consistency,<br>and speed to market.</p>

<div class="step" style="left:125px"><div class="ring"><svg width="28" height="32" viewBox="0 0 28 32" fill="none" stroke="#3a2a1c" stroke-width="2"><path d="M9 22c0-4-5-6-5-12a10 10 0 0120 0c0 6-5 8-5 12zM10 26h8M11 30h6"/></svg></div>Concept</div>
<div class="chev" style="left:195px">›</div>
<div class="step" style="left:278px"><div class="ring"><svg width="28" height="30" viewBox="0 0 28 30" fill="none" stroke="#3a2a1c" stroke-width="2"><path d="M14 28V14M14 14C8 14 3 10 3 4c6 0 11 4 11 10zM14 14c6 0 11-4 11-10-6 0-11 4-11 10z"/></svg></div>Sourcing</div>
<div class="chev" style="left:350px">›</div>
<div class="step" style="left:433px"><div class="ring"><svg width="28" height="32" viewBox="0 0 28 32" fill="none" stroke="#3a2a1c" stroke-width="2"><path d="M10 3h8M11 3v10L3 28h22L17 13V3M7 21h14"/></svg></div>R&amp;D</div>
<div class="chev" style="left:503px">›</div>
<div class="step" style="left:600px"><div class="ring"><svg width="30" height="30" viewBox="0 0 30 30" fill="none" stroke="#3a2a1c" stroke-width="2"><path d="M15 2v26M3 8l24 14M3 22 27 8M11 4l4 4 4-4M11 26l4-4 4 4"/></svg></div>Freeze Dying</div>
<div class="chev" style="left:684px">›</div>
<div class="step" style="left:767px"><div class="ring"><svg width="30" height="30" viewBox="0 0 30 30" fill="none" stroke="#3a2a1c" stroke-width="2"><path d="M15 2 27 8v14l-12 6-12-6V8zM3 8l12 6 12-6M15 14v14M9 5l12 6"/></svg></div>Packaging</div>
<div class="chev" style="left:839px">›</div>
<div class="step" style="left:921px"><div class="ring"><svg width="24" height="30" viewBox="0 0 24 30" fill="none" stroke="#3a2a1c" stroke-width="2"><rect x="3" y="2" width="18" height="26"/><path d="M8 8h2M14 8h2M8 14h2M14 14h2M10 28v-6h4v6"/></svg></div>Storage</div>
<div class="chev" style="left:993px">›</div>
<div class="step" style="left:1075px"><div class="ring"><svg width="32" height="24" viewBox="0 0 32 24" fill="none" stroke="#3a2a1c" stroke-width="2"><path d="M2 4h18v14H2zM20 9h6l4 5v4H20"/><circle cx="8" cy="19" r="3" fill="#fff"/><circle cx="24" cy="19" r="3" fill="#fff"/></svg></div>Deliveries</div>

<!-- capabilities -->
<div class="eyebrow center" style="top:2256px">CAPABILITIES</div>
<h2 class="abs center serif" style="top:2284px;font-weight:400;font-size:39px">What We Do</h2>

<article class="cap" style="left:55px">
  <div class="img" style="background:linear-gradient(180deg,#8a6a45,#b08a5c)" role="img" aria-label="Kraft pouches of freeze-dried product with loose pieces on a table"></div>
  <h4>OEM / Private Label</h4>
  <p>Lorem ipsum dolor sit amet, consectetur adipiscing elit, sed do eiusmod tempor incididunt ut labore et dolore magna aliqua. Ut enim ad minim veniam, quis nostrud exercitation</p>
  <div class="more">Learn More <svg class="arrow" viewBox="0 0 28 10"><path d="M0 5h26M21 1l5 4-5 4" stroke="#5c4631" stroke-width="1.5" fill="none"/></svg></div>
</article>
<article class="cap" style="left:428px">
  <div class="img" style="background:linear-gradient(180deg,#6e4b2c,#b58a58)" role="img" aria-label="Pile of freeze-dried nuggets on a wooden surface"></div>
  <h4>Freeze Drying</h4>
  <p>Lorem ipsum dolor sit amet, consectetur adipiscing elit, sed do eiusmod tempor incididunt ut labore et dolore magna aliqua. Ut enim ad minim veniam, quis nostrud exercitation</p>
  <div class="more">Learn More <svg class="arrow" viewBox="0 0 28 10"><path d="M0 5h26M21 1l5 4-5 4" stroke="#5c4631" stroke-width="1.5" fill="none"/></svg></div>
</article>
<article class="cap" style="left:802px">
  <div class="img" style="background:linear-gradient(180deg,#d8d4cc,#c9b79a)" role="img" aria-label="Bowls of ingredient powders with laboratory glassware"></div>
  <h4>R&amp;D Test Kitchen</h4>
  <p>Lorem ipsum dolor sit amet, consectetur adipiscing elit, sed do eiusmod tempor incididunt ut labore et dolore magna aliqua. Ut enim ad minim veniam, quis nostrud exercitation</p>
  <div class="more">Learn More <svg class="arrow" viewBox="0 0 28 10"><path d="M0 5h26M21 1l5 4-5 4" stroke="#5c4631" stroke-width="1.5" fill="none"/></svg></div>
</article>

<!-- why -->
<div class="eyebrow center" style="top:2909px">WHY BRINDLE</div>
<h2 class="abs center serif" style="top:2936px;font-weight:400;font-size:38px">Built For Quality. Designed For Scale</h2>

<div class="why" style="left:149px"><svg width="44" height="44" viewBox="0 0 44 44" fill="none" stroke="var(--gold)" stroke-width="3"><path d="M34 16A13 13 0 0010 14M10 28a13 13 0 0024 2M8 6v8h8M36 38v-8h-8"/></svg><h5>Closed-Loop<br>Manufacturing</h5><p>Lorem ipsum dolor sit amet, consectetur adipiscing elit, sed do eiusmod tempor n</p></div>
<div class="why" style="left:450px"><svg width="44" height="44" viewBox="0 0 44 44" fill="none" stroke="var(--gold)" stroke-width="3"><path d="M22 4 36 9v12c0 10-6 16-14 19C14 37 8 31 8 21V9z"/></svg><h5>Integrated Quality<br>Assurance</h5><p>Lorem ipsum dolor sit amet, consectetur adipiscing elit, sed do eiusmod tempor n</p></div>
<div class="why" style="left:752px"><svg width="44" height="44" viewBox="0 0 44 44" fill="none" stroke="var(--gold)" stroke-width="3"><circle cx="18" cy="18" r="12"/><path d="M27 27l12 12"/></svg><h5>Full<br>Traceability</h5><p>Lorem ipsum dolor sit amet, consectetur adipiscing elit, sed do eiusmod tempor n</p></div>
<div class="why" style="left:1053px"><svg width="44" height="44" viewBox="0 0 44 44" fill="none" stroke="var(--gold)" stroke-width="3"><path d="M6 40V30M14 40V24M22 40V28M30 40V18M38 40V12M6 22l10-8 8 6 14-12M30 8h8v8"/></svg><h5>Scalable<br>Production</h5><p>Lorem ipsum dolor sit amet, consectetur adipiscing elit, sed do eiusmod tempor n</p></div>

<!-- cta band -->
<section class="abs band">
  <div class="abs" style="left:0;top:0;width:110px;height:70px;border-radius:0 0 60% 0;background:rgba(255,255,255,.04)" role="img" aria-label="Faint leaf outline decoration"></div>
  <div class="abs" style="left:1090px;top:150px;width:110px;height:72px;border-radius:60% 0 0 0;background:rgba(255,255,255,.04)" role="img" aria-label="Faint leaf outline decoration"></div>
  <h2 class="serif">Lets Build Something Together</h2>
  <p>Freeze-dried meals, toppers, and treats designed for quality, consistency, and performance.</p>
  <a class="btn btn-gold" style="left:939px;top:85px;width:215px;height:62px;font-size:17px">Start A Project <svg class="arrow" viewBox="0 0 28 10"><path d="M0 5h26M21 1l5 4-5 4" stroke="#fff" stroke-width="1.5" fill="none"/></svg></a>
</section>

<!-- footer -->
<footer class="abs foot">
  <div class="abs" style="left:52px;top:74px;font-size:46px;font-weight:500;color:#fff;letter-spacing:1px">BRINDLE</div>
  <div class="abs" style="left:52px;top:124px;font-size:13px;letter-spacing:1px;color:var(--gold)">Nutrition, Frozen in Time</div>
  <p class="abs" style="left:52px;top:150px;width:250px;font-size:12px;line-height:22px;color:#c9bfb2">A fully integrated, closed-loop system from ingredient sourcing through to production, packaging, and distribution.</p>
  <span class="social" style="left:52px"></span><span class="social" style="left:101px"></span><span class="social" style="left:156px;border-radius:6px"></span>

  <h6 style="left:325px">COMPANY</h6>
  <ul style="left:325px"><li>About / Our Story</li><li>Why Brindle</li><li>Careers</li></ul>
  <h6 style="left:530px">SOLUTIONS</h6>
  <ul style="left:530px"><li>Pet Food</li><li>Agri Food</li><li>Capabilities</li></ul>
  <h6 style="left:709px">SUPPORT</h6>
  <ul style="left:709px"><li>Qualities</li><li>Contact</li></ul>
  <h6 style="left:889px">CONTACT US</h6>
  <ul style="left:889px;line-height:31px">
    <li><svg width="14" height="14" viewBox="0 0 14 14" fill="var(--gold)" style="margin-right:10px;vertical-align:-2px"><path d="M3 1l2 3-1 2c1 2 2 3 4 4l2-1 3 2-1 2C6 13 1 8 1 2z"/></svg>+1 555 014 2290</li>
    <li><svg width="14" height="11" viewBox="0 0 14 11" fill="var(--gold)" style="margin-right:10px;vertical-align:-1px"><path d="M0 0h14v11H0zM1 1l6 5 6-5" stroke="var(--foot)" stroke-width="1"/></svg>info@brindle.example</li>
    <li style="line-height:18px;padding-top:6px"><svg width="12" height="15" viewBox="0 0 12 15" fill="none" stroke="var(--gold)" stroke-width="1.6" style="margin-right:12px;vertical-align:-2px"><path d="M6 14S1 8.5 1 5.5a5 5 0 0110 0C11 8.5 6 14 6 14z"/><circle cx="6" cy="5.5" r="1.8"/></svg>48 Meadowlark Lane Harvest<br><span style="padding-left:24px">Falls, USA 00000</span></li>
  </ul>
  <div class="abs" style="left:52px;top:282px;width:1098px;height:1px;background:#5a4a3a"></div>
  <div class="abs" style="left:52px;top:308px;font-size:13px">@2026 Brindle Nutrition All Rights Reserved</div>
  <div class="abs" style="left:957px;top:308px;font-size:13px">Privacy Policy &nbsp;&nbsp;|&nbsp;&nbsp; Term Of Use</div>
</footer>

</body>
</html>
```